A Hair, Beauty and Nails Wholesalers Needs a Business Card Design

We need a business card design for our company which is being passed from parents to daughter, so we wont to re-launch the company with an updated, modern, sophisticated, elegant, chic and fresh look which still incorporates the original colour scheme of Hot Pink, Dark Grey and White. The original logo which is attached can be used on the card but we would like to see some designs with the logo and some without, as we have not yet decided if we want the logo on the card. The name of our company is 'Velmora Supplies' and the name of our website is VelmoraGlowandPolish.example.au. We specialise in supplying a massive range of Hair, Beauty and Nail products to the industry. We are based in QLD, Australia but ship many orders via our website all across Australia.

```html
<!DOCTYPE html>
<html lang="en">
<head>
<meta charset="utf-8">
<title>Velmora Supplies – Business Card</title>
<link rel="stylesheet" href="https://fonts.googleapis.com/css2?family=Quicksand:wght@400;500;600&display=swap">
<style>
  :root {
    --hot-pink: #e0358f;
    --pink-line: #e25aa3;
    --card-white: #f7f6f6;
    --backdrop: #e8e5e2;
    --shadow: rgba(60, 40, 30, 0.18);
  }
  * { margin: 0; padding: 0; box-sizing: border-box; }
  html, body { width: 1200px; height: 900px; overflow: hidden; }
  body {
    background: var(--backdrop);
    font-family: "Quicksand", sans-serif;
    color: var(--hot-pink);
    position: relative;
  }
  .card {
    position: absolute;
    top: 300px;
    width: 525px;
    height: 300px;
    background: var(--card-white);
    box-shadow: 0 6px 18px var(--shadow);
    overflow: hidden;
  }
  .card--front { left: 50px; }
  .card--back { left: 625px; }
  .card__lines {
    position: absolute;
    inset: 0;
    width: 100%;
    height: 100%;
  }
  .card__lines line, .card__lines polyline, .card__lines polygon {
    stroke: var(--pink-line);
    stroke-width: 1.2;
    fill: none;
  }

  /* Front */
  .brand-block {
    position: absolute;
    left: 24px;
    top: 70px;
    width: 160px;
    display: flex;
    align-items: center;
    gap: 8px;
  }
  .brand-dot {
    width: 16px; height: 16px;
    border-radius: 50%;
    background: var(--hot-pink);
    flex: none;
  }
  .brand-name {
    font-size: 30px;
    font-weight: 400;
    line-height: 1.15;
    color: var(--hot-pink);
  }
  .divider {
    position: absolute;
    left: 200px;
    top: 40px;
    width: 1px;
    height: 175px;
    background: var(--pink-line);
  }
  .contact {
    position: absolute;
    left: 218px;
    top: 34px;
    right: 16px;
    font-size: 18px;
    line-height: 1.4;
  }
  .contact__name {
    display: inline-block;
    font-size: 19px;
    border-bottom: 1px solid var(--pink-line);
    padding-bottom: 2px;
    margin-bottom: 8px;
  }
  .contact__role { margin-bottom: 8px; }
  .contact__street { font-weight: 600; }
  .contact__phone { margin-top: 10px; }
  .contact__phone strong { font-weight: 600; }
  .contact__email { font-size: 12.5px; }
  .website {
    position: absolute;
    left: 170px;
    bottom: 18px;
    font-size: 12.5px;
  }

  /* Back */
  .back-brand {
    position: absolute;
    left: 0; right: 0;
    top: 110px;
    display: flex;
    justify-content: center;
    align-items: center;
    gap: 12px;
  }
  .back-brand .brand-name { font-size: 38px; }
</style>
</head>
<body>

  <section class="card card--front" aria-label="Business card front">
    <svg class="card__lines" viewBox="0 0 525 300" aria-hidden="true">
      <polyline points="150,300 180,268 470,268 500,225"/>
    </svg>
    <div class="brand-block">
      <span class="brand-dot"></span>
      <span class="brand-name">Velmora<br>Supplies</span>
    </div>
    <div class="divider"></div>
    <div class="contact">
      <div class="contact__name">Dania Marlowe</div>
      <div class="contact__role">Manager, Velmora Supplies</div>
      <div class="contact__street">58 Larkspur Lane</div>
      <div>Brindlewood, QLD, <strong>4999</strong></div>
      <div class="contact__phone">Ph: <strong>(07) 5550 0182</strong></div>
      <div class="contact__email">Email: admin@velmoraglowandpolish.example.au</div>
    </div>
    <div class="website">Website: www.velmoraglowandpolish.example.au</div>
  </section>

  <section class="card card--back" aria-label="Business card back">
    <svg class="card__lines" viewBox="0 0 525 300" aria-hidden="true">
      <polygon points="110,100 190,40 395,55 440,115 400,215 125,225"/>
      <line x1="0" y1="60" x2="125" y2="225"/>
      <line x1="70" y1="300" x2="125" y2="225"/>
      <line x1="400" y1="215" x2="525" y2="230"/>
      <line x1="440" y1="115" x2="470" y2="0"/>
      <line x1="110" y1="100" x2="0" y2="150"/>
    </svg>
    <div class="back-brand">
      <span class="brand-dot"></span>
      <span class="brand-name">Velmora Supplies</span>
    </div>
  </section>

</body>
</html>
```